Cascade Rhythm Guild Business Cards

The Cascade Rhythm Guild is a non-profit organization that supports, promotes, and manages music events in the Pacific Northwest. Our mission is to keep the blues alive. We do this by partnering with local venues, schools, and national acts to bring some of the best blues music to our members. As newly elected Executive Board Members we would like to have new business cards designed. I have included a copy of our logo.

```html
<!DOCTYPE html>
<html lang="en">
<head>
<meta charset="utf-8">
<title>Cascade Rhythm Guild — Business Cards</title>
<link rel="stylesheet" href="https://fonts.googleapis.com/css2?family=Montserrat:wght@400;500;600;700&display=swap">
<style>
  :root {
    --page: #e6e6e4;
    --card: #f1f1f1;
    --card-light: #fafafa;
    --ink: #111111;
    --band: #0b0b0b;
    --accent: #6aa8e0;
    --mark-circle: #f1e48a;
    --rule: #3a3a3a;
    --faint: rgba(0, 0, 0, 0.07);
  }
  * { box-sizing: border-box; margin: 0; padding: 0; }
  html, body { width: 1200px; height: 900px; overflow: hidden; }
  body {
    background: var(--page);
    font-family: "Montserrat", sans-serif;
    color: var(--ink);
    position: relative;
  }
  .card {
    position: absolute;
    left: 337px;
    width: 525px;
    height: 300px;
    background: linear-gradient(135deg, var(--card-light), var(--card));
    box-shadow: 0 10px 24px rgba(0,0,0,0.14), 0 2px 4px rgba(0,0,0,0.08);
    overflow: hidden;
  }
  .card--front { top: 110px; }
  .card--back { top: 490px; }

  .card__band { position: absolute; left: 0; bottom: 0; width: 525px; height: 300px; }
  .card__website {
    position: absolute; right: 14px; bottom: 9px;
    color: #fff; font-size: 10px; letter-spacing: 1.2px; font-weight: 400;
  }

  .brand-mark {
    position: absolute;
    display: flex; align-items: center; gap: 10px;
  }
  .brand-mark__circle { border-radius: 50%; background: var(--mark-circle); flex: none; }
  .brand-mark__name { font-weight: 700; color: var(--ink); line-height: 1.05; }

  .card--front .brand-mark { left: 140px; top: 92px; }
  .card--front .brand-mark__circle { width: 70px; height: 70px; }
  .card--front .brand-mark__name { font-size: 22px; width: 150px; }

  .card--back .brand-mark { left: 22px; top: 20px; }
  .card--back .brand-mark__circle { width: 34px; height: 34px; }
  .card--back .brand-mark__name { font-size: 11px; width: 80px; }

  .brand-mark--faint { left: 300px !important; top: 22px !important; }
  .brand-mark--faint .brand-mark__circle { background: var(--faint); width: 54px !important; height: 54px !important; }
  .brand-mark--faint .brand-mark__name { color: var(--faint); font-size: 16px !important; width: 110px !important; }

  .holder { position: absolute; left: 60px; top: 96px; }
  .holder__name { font-size: 22px; font-weight: 600; letter-spacing: 0.3px; }
  .holder__role { font-size: 12px; color: var(--accent); font-weight: 500; margin-top: 1px; }

  .divider { position: absolute; left: 60px; right: 22px; top: 146px; height: 1px; background: var(--rule); }

  .org-title {
    position: absolute; right: 22px; top: 160px;
    font-size: 17px; font-weight: 500; letter-spacing: 0.2px;
  }

  .contacts { position: absolute; left: 30px; top: 156px; display: flex; gap: 10px; }
  .contacts__icons { width: 22px; height: 118px; }
  .contacts__list { list-style: none; color: var(--accent); font-size: 9.5px; line-height: 1.35; letter-spacing: 0.5px; padding-top: 2px; }
  .contacts__list li { margin-bottom: 3px; }
</style>
</head>
<body>

<section class="card card--front" aria-label="Card front">
  <div class="brand-mark">
    <span class="brand-mark__circle"></span>
    <span class="brand-mark__name">Cascade Rhythm Guild</span>
  </div>
  <svg class="card__band" viewBox="0 0 525 300" aria-hidden="true">
    <polyline points="0,287 332,287 356,268" fill="none" stroke="var(--accent)" stroke-width="3"/>
    <polygon points="0,300 0,292 336,292 362,270 525,270 525,300" fill="var(--band)"/>
  </svg>
  <span class="card__website">www.website.com</span>
</section>

<section class="card card--back" aria-label="Card back">
  <div class="brand-mark">
    <span class="brand-mark__circle"></span>
    <span class="brand-mark__name">Cascade Rhythm Guild</span>
  </div>
  <div class="brand-mark brand-mark--faint" aria-hidden="true">
    <span class="brand-mark__circle"></span>
    <span class="brand-mark__name">Cascade Rhythm Guild</span>
  </div>

  <div class="holder">
    <p class="holder__name">Your Name</p>
    <p class="holder__role">Project Manager</p>
  </div>
  <div class="divider"></div>
  <h1 class="org-title">CASCADE RHYTHM GUILD</h1>

  <div class="contacts">
    <svg class="contacts__icons" viewBox="0 0 22 118" aria-hidden="true">
      <line x1="11" y1="8" x2="11" y2="108" stroke="var(--ink)" stroke-width="1.5"/>
      <circle cx="11" cy="10" r="8" fill="var(--ink)"/>
      <path d="M8 7 q0 6 6 6 l1 -2 -2 -1 -1 1 q-2 -1 -3 -3 l1 -1 -1 -2z" fill="#fff"/>
      <circle cx="11" cy="42" r="8" fill="var(--ink)"/>
      <path d="M11 46 l-3 -4 a3 3 0 1 1 6 0z" fill="#fff"/>
      <circle cx="11" cy="74" r="8" fill="var(--ink)"/>
      <rect x="7" y="71" width="8" height="6" fill="none" stroke="#fff" stroke-width="1"/>
      <polyline points="7,71 11,74 15,71" fill="none" stroke="#fff" stroke-width="1"/>
      <circle cx="11" cy="106" r="8" fill="var(--ink)"/>
      <text x="11" y="109.5" text-anchor="middle" font-size="10" fill="#fff" font-family="Montserrat, sans-serif">@</text>
    </svg>
    <ul class="contacts__list">
      <li>123456789</li>
      <li>your adresse.town<br>city.country</li>
      <li>your mail .com</li>
      <li>www.website.com<br>www.social.net/yours</li>
    </ul>
  </div>

  <svg class="card__band" viewBox="0 0 525 300" aria-hidden="true">
    <polyline points="0,287 332,287 356,268" fill="none" stroke="var(--accent)" stroke-width="3"/>
    <polygon points="0,300 0,292 336,292 362,270 525,270 525,300" fill="var(--band)"/>
  </svg>
  <span class="card__website">www.website.com</span>
</section>

</body>
</html>
```